Tarnvik Business Card Design - double sided -plumbing local plumbing company

We have a Plumbing company where the design was create through Pixel Harbour. We would now like a business card designed as well. We want it to be in the colour version of the logo.

Details below for the card.

Phone Number: 0468 215 307
Email: info@tarnvikplumbing.example.au
Website: https://tarnvikplumbing.example.au
We really want a sophisticated design that stand out from the other- informative and timeless.

Target Market(s)

local Canberra market

Industry/Entity Type

Plumbing, gas fitting, hot water

Contact Information for Business Card

Phone number, email, logo and "Supplying all your heating, cooling and hot water needs"

Requirements
Must have
• bust be colourful, must also be though about it being printed on a magnet. must Vik with the logo - I dont want the logo and information chucked onto a white canvas I would prefer it to be smooth and look purposeful

```html
<!DOCTYPE html>
<html lang="en">
<head>
<meta charset="utf-8">
<title>Tarnvik Business Card</title>
<link href="https://fonts.googleapis.com/css2?family=Arimo:wght@400;700&display=swap" rel="stylesheet">
<style>
  :root {
    --orange: #f9ae42;
    --blue: #04a9e8;
    --white: #ffffff;
    --ink-blue: #0aa0de;
    --page: #e9eaec;
  }
  * { margin: 0; padding: 0; box-sizing: border-box; }
  html, body { width: 1200px; height: 874px; overflow: hidden; }
  body {
    background: var(--page);
    font-family: "Arimo", Arial, sans-serif;
    display: flex;
    flex-direction: column;
    align-items: center;
    justify-content: center;
    gap: 44px;
  }
  .card {
    position: relative;
    width: 560px;
    height: 342px;
    border-radius: 22px;
    overflow: hidden;
    box-shadow: 0 6px 18px rgba(0,0,0,0.18);
  }
  /* Front */
  .card-front { background: var(--orange); color: var(--white); }
  .front-brand {
    position: absolute;
    left: 0; right: 0; top: 108px;
    text-align: center;
    font-weight: 700;
    font-size: 82px;
    letter-spacing: 2px;
  }
  .front-tagline {
    position: absolute;
    left: 0; right: 0; top: 250px;
    text-align: center;
    font-size: 15px;
  }
  .front-tagline strong { font-weight: 700; font-style: italic; }
  /* Back */
  .card-back { background: var(--white); }
  .back-shapes { position: absolute; inset: 0; }
  .back-brand {
    position: absolute;
    left: 36px; top: 42px;
    font-weight: 700;
    font-size: 46px;
    letter-spacing: 1px;
    color: var(--ink-blue);
  }
  .contact-name {
    position: absolute;
    right: 40px; top: 108px;
    text-align: right;
    color: var(--white);
  }
  .contact-name .name { font-weight: 700; font-size: 24px; }
  .contact-name .role { font-size: 15px; margin-top: 2px; }
  .contact-list {
    position: absolute;
    right: 34px; bottom: 40px;
    list-style: none;
    color: var(--white);
    font-size: 15px;
    text-align: right;
  }
  .contact-list li {
    display: flex;
    align-items: center;
    justify-content: flex-end;
    gap: 12px;
    line-height: 24px;
  }
  .contact-list svg { width: 14px; height: 14px; flex: none; }
</style>
</head>
<body>
  <section class="card card-front">
    <div class="front-brand">TARNVIK</div>
    <p class="front-tagline">Supplying all your <strong>heating, cooling</strong> and <strong>hot water</strong> needs</p>
  </section>

  <section class="card card-back">
    <svg class="back-shapes" viewBox="0 0 560 342" preserveAspectRatio="none">
      <path fill="var(--orange)" d="M340 0 L560 0 L560 342 L258 342 C200 310 186 258 192 220 C198 174 232 140 274 100 Z"/>
      <path fill="var(--blue)" d="M360 0 L560 0 L560 342 L276 342 C224 310 212 262 218 226 C224 184 254 150 296 108 Z"/>
    </svg>
    <div class="back-brand">TARNVIK</div>
    <div class="contact-name">
      <div class="name">ELIN MARSH</div>
      <div class="role">President</div>
    </div>
    <ul class="contact-list">
      <li>0468 215 307
        <svg viewBox="0 0 24 24"><path fill="#fff" d="M6.6 10.8a15 15 0 0 0 6.6 6.6l2.2-2.2a1 1 0 0 1 1-.25 11.4 11.4 0 0 0 3.6.57 1 1 0 0 1 1 1V20a1 1 0 0 1-1 1A17 17 0 0 1 3 4a1 1 0 0 1 1-1h3.5a1 1 0 0 1 1 1c0 1.25.2 2.45.57 3.57a1 1 0 0 1-.25 1z"/></svg>
      </li>
      <li>info@tarnvikplumbing.example.au
        <svg viewBox="0 0 24 24"><rect x="2" y="5" width="20" height="14" rx="1" fill="#fff"/><path d="M3 6l9 7 9-7" fill="none" stroke="var(--blue)" stroke-width="1.8"/></svg>
      </li>
      <li>www.tarnvikplumbing.example.au
        <svg viewBox="0 0 24 24"><circle cx="12" cy="12" r="10" fill="#fff"/><path d="M2 12h20M12 2c3 3 3 17 0 20M12 2c-3 3-3 17 0 20" fill="none" stroke="var(--blue)" stroke-width="1.4"/></svg>
      </li>
    </ul>
  </section>
</body>
</html>
```